Business Card Design Project

Business card design for an IT Service company. A logo has already been created in a different contest and has been attached to this project. Ideally we're looking for a double sided business card that matches the look and feel of our newly created logo.

We're open to creativity if you feel a tag line is needed such as "IT Services and Application Development". We're open to really and look and feel - even single sided business cards if you feel you have something that's a great idea.

Last thought here - I'm not sure how it'll look but maybe a two tone card? One side dark blue and the other side white? Don't limit the design submissions to this tho - just curious if it would look good

Nothing too busy please - simple... Thank you and happy designing!

Target Market(s)

Businesses that require IT Services and support for hosted services, technical consultation, web design.

Industry/Entity Type

Business

Font styles to use
Sans Serif

Requirements
Must have
• Use the colors provided in the logo (see attachment) or additional colors that compliment
Must have the following contact info (not necessarily in this order):
- Owen Marsh
- Founding Partner
- omarsh@velomarquin.com
- 555-271-3948
- www.velomarquin.com

```html
<!DOCTYPE html>
<html lang="en">
<head>
<meta charset="utf-8">
<title>VeloMarquin — Business Card</title>
<link rel="stylesheet" href="https://fonts.googleapis.com/css2?family=Arimo:ital,wght@0,400;0,700;1,400&display=swap">
<style>
  :root {
    --navy: #06113f;
    --white: #ffffff;
    --green: #5db31f;
    --blue: #2b7de1;
  }
  html, body {
    margin: 0;
    padding: 0;
    overflow: hidden;
    background: var(--white);
  }
  .card {
    position: relative;
    width: 1200px;
    height: 734px;
    box-sizing: border-box;
    background: var(--white);
    border: 34px solid var(--navy);
    font-family: "Arimo", Arial, sans-serif;
    color: var(--navy);
    overflow: hidden;
  }
  .brand {
    position: absolute;
    left: 0;
    right: 0;
    top: 180px;
    text-align: center;
    font-weight: 700;
    font-size: 98px;
    line-height: 1;
    letter-spacing: -1px;
    color: var(--navy);
  }
  .identity {
    position: absolute;
    left: 0;
    right: 0;
    top: 400px;
    text-align: center;
  }
  .identity__name {
    margin: 0;
    font-weight: 400;
    font-size: 52px;
    line-height: 1.1;
  }
  .identity__title {
    margin: 4px 0 0;
    font-size: 34px;
    line-height: 1.1;
  }
  .contact {
    position: absolute;
    left: 0;
    right: 0;
    top: 610px;
    display: flex;
    justify-content: center;
    gap: 42px;
    font-size: 25px;
    line-height: 1;
  }
  .contact__label {
    font-weight: 700;
    margin-right: 8px;
  }
  .contact__value {
    font-style: italic;
  }
</style>
</head>
<body>
  <div class="card">
    <div class="brand">VeloMarquin</div>

    <div class="identity">
      <h1 class="identity__name">Owen Marsh</h1>
      <p class="identity__title">Founding Partner</p>
    </div>

    <div class="contact">
      <span class="contact__item"><span class="contact__label">T</span><span class="contact__value">555-271-3948</span></span>
      <span class="contact__item"><span class="contact__label">E</span><span class="contact__value">omarsh@velomarquin.com</span></span>
      <span class="contact__item"><span class="contact__label">W</span><span class="contact__value">www.velomarquin.com</span></span>
    </div>
  </div>
</body>
</html>
```